3 x Webpage Homepage Banner for New Scrap Metal Company website

New website (currently under construction) for a scrap metal recycling company require 3 home page banner that give visitor have a sense of confident and relevance in the company. Feeling good about the products and value.

I have attached here a file name "website home page" to show the currently general idea of the design of the webpage. Two more file "Regular Login 1" and "Regular Login 2" to show the currently "looks" when a user visit the page. The current banner is a dummy.

One of the file titled "Company Image" is the picture of our company which I would also like to have it in one of the banner.

```html
<!DOCTYPE html>
<html lang="en">
<head>
<meta charset="utf-8">
<title>Harbor Steel Recycling – Homepage Banners</title>
<link rel="stylesheet" href="https://fonts.googleapis.com/css2?family=Roboto:wght@300;400;500;700&display=swap">
<style>
  :root {
    --board: #f2cd76;
    --white: #ffffff;
    --gold: #c8952a;
    --gold-band-top: #e2b04a;
    --gold-band-bottom: #c99530;
    --gold-line: #d8a53c;
    --cart-blue: #0f4879;
    --nav-text: #ffffff;
    --hero-text: #ffffff;
    --search-border: #c9c9c9;
    --search-text: #a8a8a8;
  }
  * { box-sizing: border-box; margin: 0; padding: 0; }
  html, body {
    width: 1108px; height: 1200px; overflow: hidden;
    background: var(--board);
    font-family: "Roboto", sans-serif;
  }
  .board { position: relative; width: 1108px; height: 1200px; }

  .banner {
    position: absolute; left: 115px; width: 877px; height: 347px;
    background: var(--white);
    box-shadow: 10px 12px 18px rgba(120, 85, 20, 0.35);
    overflow: hidden;
  }
  .banner--one { top: 42px; }
  .banner--two { top: 427px; }
  .banner--three { top: 810px; }

  .site-header { position: relative; height: 38px; background: var(--white); }
  .brand {
    position: absolute; left: 202px; top: 13px;
    display: flex; align-items: center; gap: 6px;
    color: var(--gold); font-weight: 500; font-size: 9px; letter-spacing: 0.5px;
    text-transform: uppercase;
  }
  .brand-mark { width: 13px; height: 13px; background: var(--gold); }
  .search {
    position: absolute; left: 410px; top: 12px; width: 146px; height: 15px;
    border: 1px solid var(--search-border); border-radius: 8px;
    font-size: 6px; color: var(--search-text);
    padding: 3px 0 0 9px;
  }
  .search svg { position: absolute; right: 8px; top: 3px; }
  .cart {
    position: absolute; left: 579px; top: 0; width: 94px; height: 29px;
    background: var(--cart-blue); border-radius: 0 0 4px 4px;
    color: var(--white); display: flex; align-items: center; gap: 6px; padding-left: 14px;
  }
  .cart-label { font-size: 5.5px; line-height: 7px; }
  .cart-label strong { font-weight: 700; display: block; }

  .main-nav {
    position: relative; height: 18px;
    background: linear-gradient(var(--gold-band-top), var(--gold-band-bottom));
    display: flex; align-items: center; padding-left: 203px;
    font-size: 5.5px; font-weight: 500; color: var(--nav-text); letter-spacing: 0.2px;
  }
  .main-nav span { margin-right: 16px; }
  .main-nav .current { font-weight: 700; border-bottom: 1px solid var(--white); padding-bottom: 1px; }
  .login { position: absolute; left: 642px; display: flex; align-items: center; gap: 4px; }

  .hero { position: relative; height: 291px; color: var(--hero-text); }
  .hero-photo { position: absolute; inset: 0; }
  .hero--building .hero-photo {
    background:
      linear-gradient(180deg, rgba(40,40,40,0) 0%, rgba(40,40,40,0) 52%, rgba(30,30,30,0.55) 62%, rgba(20,20,20,0.75) 100%) 380px 0 / 497px 100% no-repeat,
      linear-gradient(180deg, #3e3e3e 0%, #4a4a4a 12%, #cfcfcf 22%, #bdbdbd 45%, #9a9a9a 55%) 380px 0 / 497px 100% no-repeat,
      linear-gradient(100deg, #6a6a6a 0%, #727272 45%, #8a8a8a 60%, #888 100%);
  }
  .hero--building .hero-photo::after {
    content: ""; position: absolute; inset: 0;
    background: linear-gradient(90deg, #707070 0%, #747474 42%, rgba(116,116,116,0.6) 52%, rgba(116,116,116,0) 62%);
  }
  .hero--yard .hero-photo {
    background:
      radial-gradient(ellipse 70px 110px at 480px 170px, #d0d0d0 0%, #8a8a8a 50%, rgba(0,0,0,0) 100%),
      radial-gradient(ellipse 90px 120px at 640px 190px, #9a9a9a 0%, #4a4a4a 55%, rgba(0,0,0,0) 100%),
      radial-gradient(ellipse 110px 150px at 810px 130px, #d8d8d8 0%, #7a7a7a 45%, rgba(0,0,0,0) 100%),
      linear-gradient(100deg, #000 0%, #030303 46%, #1a1a1a 60%, #2a2a2a 100%);
  }
  .hero--scrap .hero-photo {
    background:
      repeating-radial-gradient(ellipse 22px 12px at 30% 40%, rgba(255,255,255,0.05) 0 4px, rgba(0,0,0,0.12) 4px 9px),
      radial-gradient(ellipse at 70% 40%, #4a4a4a 0%, #2e2e2e 50%, #181818 100%);
  }
  .hero-copy { position: absolute; left: 107px; top: 74px; }
  .hero-title { font-size: 29px; line-height: 33px; font-weight: 400; }
  .hero-tagline { font-size: 15px; font-weight: 300; margin-top: 6px; }
  .hero--yard .hero-sub { font-size: 20px; font-weight: 300; line-height: 26px; }
  .hero--scrap .hero-copy { left: 0; right: 0; top: 77px; text-align: center; }
  .hero--scrap .hero-title { font-size: 29px; font-weight: 700; }
  .hero--scrap .hero-list { font-size: 18px; font-weight: 300; line-height: 31px; margin-top: 2px; }
  .hero-rule { position: absolute; left: 0; right: 0; top: 273px; height: 2px; background: var(--gold-line); }
</style>
</head>
<body>
<div class="board">

  <section class="banner banner--one">
    <header class="site-header">
      <div class="brand"><span class="brand-mark"></span>Harbor Steel Recycling</div>
      <div class="search">Search
        <svg width="7" height="7" viewBox="0 0 7 7"><circle cx="3" cy="3" r="2.2" fill="none" stroke="#bbb" stroke-width="0.8"/><line x1="4.6" y1="4.6" x2="6.6" y2="6.6" stroke="#bbb" stroke-width="0.8"/></svg>
      </div>
      <div class="cart">
        <svg width="15" height="12" viewBox="0 0 15 12"><path d="M1 1h2l2 7h7l2-5H4" fill="none" stroke="#fff" stroke-width="1.1"/><circle cx="6" cy="10.5" r="1" fill="#fff"/><circle cx="11" cy="10.5" r="1" fill="#fff"/></svg>
        <div class="cart-label"><strong>MY CART</strong>0 items - SGD 0.00</div>
      </div>
    </header>
    <nav class="main-nav">
      <span class="current">HOME</span><span>ABOUT US</span><span>PRODUCTS</span><span>OUR SERVICES</span><span>INVESTORS</span><span>CONTACT US</span>
      <div class="login"><svg width="6" height="6" viewBox="0 0 6 6"><circle cx="3" cy="1.8" r="1.5" fill="#fff"/><path d="M0.5 6a2.5 2.2 0 0 1 5 0z" fill="#fff"/></svg>LOG IN</div>
    </nav>
    <div class="hero hero--building">
      <div class="hero-photo" role="img" aria-label="Black and white photo of the company's warehouse building seen from below"></div>
      <div class="hero-copy">
        <h1 class="hero-title">Recycling<br>Industrial Metal Scraps</h1>
        <p class="hero-tagline">We are the leading industry scrap provider.</p>
      </div>
    </div>
  </section>

  <section class="banner banner--two">
    <header class="site-header">
      <div class="brand"><span class="brand-mark"></span>Harbor Steel Recycling</div>
      <div class="search">Search
        <svg width="7" height="7" viewBox="0 0 7 7"><circle cx="3" cy="3" r="2.2" fill="none" stroke="#bbb" stroke-width="0.8"/><line x1="4.6" y1="4.6" x2="6.6" y2="6.6" stroke="#bbb" stroke-width="0.8"/></svg>
      </div>
      <div class="cart">
        <svg width="15" height="12" viewBox="0 0 15 12"><path d="M1 1h2l2 7h7l2-5H4" fill="none" stroke="#fff" stroke-width="1.1"/><circle cx="6" cy="10.5" r="1" fill="#fff"/><circle cx="11" cy="10.5" r="1" fill="#fff"/></svg>
        <div class="cart-label"><strong>MY CART</strong>0 items - SGD 0.00</div>
      </div>
    </header>
    <nav class="main-nav">
      <span class="current">HOME</span><span>ABOUT US</span><span>PRODUCTS</span><span>OUR SERVICES</span><span>INVESTORS</span><span>CONTACT US</span>
      <div class="login"><svg width="6" height="6" viewBox="0 0 6 6"><circle cx="3" cy="1.8" r="1.5" fill="#fff"/><path d="M0.5 6a2.5 2.2 0 0 1 5 0z" fill="#fff"/></svg>LOG IN</div>
    </nav>
    <div class="hero hero--yard">
      <div class="hero-photo" role="img" aria-label="Black and white photo of stacked bales of compressed scrap metal in a yard"></div>
      <div class="hero-copy">
        <h1 class="hero-title">AUTHORIZED</h1>
        <p class="hero-sub">Fully Equipped Scrap Yard</p>
      </div>
      <div class="hero-rule"></div>
    </div>
  </section>

  <section class="banner banner--three">
    <header class="site-header">
      <div class="brand"><span class="brand-mark"></span>Harbor Steel Recycling</div>
      <div class="search">Search
        <svg width="7" height="7" viewBox="0 0 7 7"><circle cx="3" cy="3" r="2.2" fill="none" stroke="#bbb" stroke-width="0.8"/><line x1="4.6" y1="4.6" x2="6.6" y2="6.6" stroke="#bbb" stroke-width="0.8"/></svg>
      </div>
      <div class="cart">
        <svg width="15" height="12" viewBox="0 0 15 12"><path d="M1 1h2l2 7h7l2-5H4" fill="none" stroke="#fff" stroke-width="1.1"/><circle cx="6" cy="10.5" r="1" fill="#fff"/><circle cx="11" cy="10.5" r="1" fill="#fff"/></svg>
        <div class="cart-label"><strong>MY CART</strong>0 items - SGD 0.00</div>
      </div>
    </header>
    <nav class="main-nav">
      <span class="current">HOME</span><span>ABOUT US</span><span>PRODUCTS</span><span>OUR SERVICES</span><span>INVESTORS</span><span>CONTACT US</span>
      <div class="login"><svg width="6" height="6" viewBox="0 0 6 6"><circle cx="3" cy="1.8" r="1.5" fill="#fff"/><path d="M0.5 6a2.5 2.2 0 0 1 5 0z" fill="#fff"/></svg>LOG IN</div>
    </nav>
    <div class="hero hero--scrap">
      <div class="hero-photo" role="img" aria-label="Dark close-up photo of a heap of small metal scrap pieces"></div>
      <div class="hero-copy">
        <h1 class="hero-title">SCRAP METAL RECYCLING</h1>
        <p class="hero-list">Ferrous &nbsp;|&nbsp; Non-Ferrous &nbsp;|&nbsp; Machineries<br>Electronics &nbsp;|&nbsp; Industrial</p>
      </div>
      <div class="hero-rule"></div>
    </div>
  </section>

</div>
</body>
</html>
```